Detox Drink Needs A Label for a drug testing company

About Us
The company name is “Pillwise”, we are a diagnostic test provider specialising in the distribution and manufacturing of drug testing kits. Our end user is both commercial and private clients with over 70% being the later of the two.

About the product
The product I am marketing is a urine detox drink aimed at removing drug metabolites from the urine, there are currently a number of similar products on the market; Veltroprime, Falcor Brisq, Renoquill, none of which are made in Australia.

We are looking to enter this market with an Australia made and owned product that works in much the same way
but is available locally for distribution.

We currently have another product on the market which works in much the same way but to remove drug metabolites from the saliva in order to prevent false positives on a drugntest.

The urine cleanse will work by diuretic action, promoting urination by osmotic release,effectively diluting drug metabolites.

What we are after
What we are after is a label to suit a 500ML bottle that contains various information including company logo, nutritional Information which will need to be editable, size, flavour etc. Product name – Urine Cleanse / Purge – Lite Flavour – Watermelon , Grape

We would like to keep a professional but modern look that makes our product come across as more pharmaceutical rather than the energy drink look that our competitors are running
with.

Industry/Entity Type

Health Product

Colors
33a6d7
f3f1f8
fbf289
33b8a4

Requirements
Must have
• Flavour; Grape, Watermelon, Lemon Line (must be editable text)
• Brand Logo
• Colorful Graphics
• Full wrap around label
• Nutritional Information on the rear with editable text
• Urine Cleanse
• Helps to cleanse the urine of drug metabolites

```html
<!DOCTYPE html>
<html lang="en">
<head>
<meta charset="utf-8">
<title>Pillwise Urine Cleanse – Grape Label</title>
<link rel="stylesheet" href="https://fonts.googleapis.com/css2?family=Roboto:wght@500;700;900&family=Kalam:wght@400&display=swap">
<style>
  :root {
    --sky-blue: #33a6d7;
    --sky-deep: #1f7fc4;
    --label-white: #f3f1f8;
    --paper: #fbfbfd;
    --soft-yellow: #fbf289;
    --teal: #33b8a4;
    --teal-text: #2f9a8c;
    --amber: #f4a21c;
    --amber-deep: #e8860c;
    --ink: #1a1a1a;
    --mid-grey: #d9dce2;
  }
  html, body {
    margin: 0;
    padding: 0;
    width: 1200px;
    height: 2931px;
    overflow: hidden;
    background: var(--paper);
  }
  .label {
    position: relative;
    width: 1200px;
    height: 2931px;
    overflow: hidden;
    background: linear-gradient(180deg, var(--label-white) 0%, #ffffff 40%, var(--mid-grey) 100%);
    font-family: "Roboto", Arial, sans-serif;
  }
  .wave-band {
    position: absolute;
    left: 0;
    width: 1200px;
  }
  .wave-band--sky {
    top: 0;
    height: 1050px;
    background:
      radial-gradient(ellipse 900px 160px at 40% 620px, rgba(51,166,215,0.55), rgba(51,166,215,0) 70%),
      linear-gradient(180deg, var(--sky-deep) 0%, var(--sky-blue) 22%, #bfe2f3 55%, rgba(243,241,248,0) 100%);
  }
  .wave-band--amber {
    top: 1780px;
    height: 900px;
    background:
      radial-gradient(ellipse 800px 170px at 55% 300px, rgba(244,162,28,0.55), rgba(244,162,28,0) 70%),
      linear-gradient(180deg, rgba(251,242,137,0) 0%, rgba(251,242,137,0.8) 25%, var(--amber) 70%, var(--amber-deep) 100%);
  }
  .brand {
    position: absolute;
    top: 470px;
    left: 50%;
    transform: translateX(-50%);
    display: flex;
    align-items: center;
    gap: 36px;
    padding: 40px 90px;
    background: var(--paper);
    border: 6px solid var(--ink);
    border-radius: 130px;
  }
  .brand__dot {
    width: 90px;
    height: 90px;
    border-radius: 50%;
    background: var(--teal);
  }
  .brand__name {
    font-family: "Roboto", Arial, sans-serif;
    font-weight: 700;
    font-size: 110px;
    color: var(--ink);
    letter-spacing: 2px;
  }
  .product-name {
    position: absolute;
    top: 1150px;
    width: 100%;
    text-align: center;
    margin: 0;
    font-weight: 700;
    font-size: 190px;
    color: var(--ink);
    letter-spacing: -2px;
  }
  .flavour {
    position: absolute;
    top: 1530px;
    width: 100%;
    text-align: center;
    margin: 0;
    font-family: "Kalam", cursive;
    font-weight: 400;
    font-size: 130px;
    color: var(--teal-text);
    letter-spacing: 4px;
  }
  .claim {
    position: absolute;
    top: 2680px;
    left: 0;
    width: 1200px;
    height: 251px;
    display: flex;
    align-items: center;
    justify-content: center;
    background: var(--amber-deep);
    margin: 0;
    font-weight: 700;
    font-size: 52px;
    color: var(--ink);
  }
</style>
</head>
<body>
  <main class="label">
    <div class="wave-band wave-band--sky" role="img" aria-label="Flowing blue wave lines across a sky gradient"></div>
    <div class="wave-band wave-band--amber" role="img" aria-label="Flowing orange and yellow wave lines"></div>

    <div class="brand">
      <span class="brand__dot"></span>
      <span class="brand__name">Pillwise</span>
    </div>

    <h1 class="product-name">Urine Cleanse</h1>
    <p class="flavour">Grape Flavour</p>

    <p class="claim">Helps to cleanse the urine of drug metabolites</p>
  </main>
</body>
</html>
```